New profile page for existing party website

For the party website 'Brindlepost' we need a new design for the user profile page.

The page should show
* a profile picture
* basic information like name, age and city
* music styles he/she likes
* links to their social link profile and website
* a bio (HTML content)
* events they plan to go to
* past events
* pictures

Challenge is that some users may have little information (just their name) while others have a huge description, lots of foto's, events, etc.

Please visit http://www.brindlepost.example and http://www.brindlepost.example/users/tobias

Target Market(s)

Men and women between 18 and 35

Industry/Entity Type

Night Club

Number of Pages Required

2 page

Font styles to use
Other font styles liked:
• Roboto

Requirements
Must have
• Please design how the page looks with a fully filled out profile and with an empty profile.
• It should fit well with the existing website.
• Include designs for both for small screens (mobile) and large screens (tablet, desktop).
Nice to have
• UX design on how to collapse or paginate sections.
• Interactive effects would be a bonus.
Should not have
• The page should not have subnavigation like menus or tabs.

```html
<!DOCTYPE html>
<html lang="nl">
<head>
<meta charset="utf-8">
<title>Brindlepost – Profiel Tobias Verbrugge</title>
<link href="https://fonts.googleapis.com/css2?family=Roboto:wght@300;400;500;700&display=swap" rel="stylesheet">
<style>
:root{
  --ink:#111111;
  --bar:#141414;
  --text:#222222;
  --line:#d9d9d9;
  --white:#ffffff;
  --hero-a:#f3905a;
  --hero-b:#f0708a;
  --hero-c:#f6b3a3;
  --page:#ffffff;
}
*{box-sizing:border-box;margin:0;padding:0}
html,body{width:1200px;height:4945px;overflow:hidden}
body{font-family:'Roboto',sans-serif;color:var(--text);background:var(--page);position:relative}

/* top navigation */
.topnav{height:53px;background:var(--bar);display:flex;align-items:center;padding:0 18px;color:var(--white)}
.brand{display:flex;align-items:center;gap:8px;font-size:24px;font-weight:500;color:var(--white)}
.brand-mark{width:14px;height:14px;background:var(--hero-b)}
.menu{display:flex;gap:24px;margin-left:auto;font-size:15px;color:#cfcfcf}
.search{margin-left:22px;width:130px;height:28px;background:var(--white);border-radius:3px;color:#999;font-size:13px;padding:6px 8px}
.account{display:flex;align-items:center;gap:10px;margin-left:26px;font-size:15px}
.account-photo{width:36px;height:36px;background:linear-gradient(135deg,#c98a5c,#e7623f)}

/* hero */
.hero{height:345px;position:relative;background:linear-gradient(100deg,var(--hero-a) 0%,var(--hero-b) 45%,var(--hero-c) 100%);color:var(--white)}
.hero-photo{position:absolute;left:133px;top:50px;width:200px;height:205px;background:linear-gradient(160deg,#e8e2d6,#b08a6a);border:4px solid rgba(255,255,255,.85)}
.hero-info{position:absolute;left:425px;top:62px}
.hero-name{font-size:40px;font-weight:300;letter-spacing:.5px;line-height:46px}
.hero-since{font-size:13px;margin:4px 0 14px;opacity:.95}
.hero-fact{font-size:18px;font-weight:500;line-height:28px}
.hero-links{display:flex;gap:14px;margin-top:22px}
.hero-links span{width:28px;height:28px;border:2px solid var(--white);border-radius:4px}
.edit-btn{position:absolute;right:26px;top:26px;background:rgba(255,255,255,.9);color:#444;font-size:13px;padding:7px 16px;border-radius:3px}

/* sections */
.section{margin:0 17px}
.section-head{height:46px;background:var(--bar);color:var(--white);display:flex;align-items:center;justify-content:space-between;padding:0 0 0 16px;font-size:20px;font-weight:700}
.toggle{width:46px;height:46px;display:flex;align-items:center;justify-content:center}
.bio{margin-top:4px}
.bio-body{height:1030px;overflow:hidden;padding:26px 14px 0;font-size:14px;line-height:22px}
.bio-body h3{font-size:15px;font-weight:700;margin-bottom:22px}
.bio-body p{margin-bottom:22px}
.bio-body strong{font-weight:700}
.events{margin-top:20px}
.event-list{padding:20px 0}
.event{height:185px;display:flex;padding:20px 0 0 116px;border-bottom:1px solid var(--line)}
.event:last-child{border-bottom:none}
.poster{position:relative;width:280px;height:115px;flex:none}
.poster .date{position:absolute;right:6px;top:6px;background:rgba(255,255,255,.92);font-size:11px;font-weight:700;padding:3px 6px;color:#333}
.p-green{background:linear-gradient(90deg,#1b8f3c,#2f6e3a)}
.p-teal{background:linear-gradient(90deg,#bfe5df,#e7f4f1)}
.p-bright{background:linear-gradient(90deg,#f7f3ea,#f4d0c4)}
.p-navy{background:#1e2f3d}
.event-text{margin-left:28px;padding-top:2px}
.event-title{font-size:15px;font-weight:700;margin-bottom:8px}
.event-row{display:flex;align-items:center;gap:10px;font-size:13px;line-height:22px;font-weight:500}
.event-row svg{width:14px;height:14px;flex:none}

/* photos */
.photos{margin-top:20px}
.photo-grid{height:900px;padding-top:10px;display:grid;grid-template-columns:290px repeat(4,1fr);grid-template-rows:repeat(4,1fr);gap:8px}
.photo-grid div{background:linear-gradient(150deg,#e8a35a,#e06a2e)}
.photo-grid .tall{grid-row:span 2}
.photo-grid .alt{background:linear-gradient(150deg,#cfc7bb,#e58542)}
.photo-grid .dark{background:linear-gradient(150deg,#3a3330,#d4773a)}

/* footer */
.footer{position:absolute;left:0;bottom:0;width:1200px;height:85px;background:var(--ink);color:var(--white);text-align:center;padding-top:24px}
.footer-links{font-size:13px;font-weight:700;letter-spacing:.5px}
.footer-copy{font-size:11px;color:#aaa;margin-top:8px}
</style>
</head>
<body>

<header class="topnav">
  <div class="brand"><span class="brand-mark"></span>Brindlepost</div>
  <nav class="menu"><span>Home</span><span>Agenda</span><span>Vrijkaarten</span><span>Foto's</span><span>Nieuws</span></nav>
  <div class="search">Zoeken</div>
  <div class="account"><div class="account-photo" role="img" aria-label="Profielfoto van de ingelogde gebruiker"></div>Tobias Verbrugge</div>
</header>

<section class="hero">
  <div class="hero-photo" role="img" aria-label="Profielfoto van Tobias Verbrugge"></div>
  <div class="hero-info">
    <div class="hero-name">Tobias Verbrugge</div>
    <div class="hero-since">Member since Mei 24, 2006</div>
    <div class="hero-fact">Age - 34</div>
    <div class="hero-fact">City - Amsterdam</div>
    <div class="hero-fact">Music - Latin / Salsa</div>
    <div class="hero-links"><span></span><span></span><span></span><span></span></div>
  </div>
  <div class="edit-btn">Wijzigen</div>
</section>

<section class="section bio">
  <div class="section-head">Biography
    <span class="toggle"><svg width="22" height="14" viewBox="0 0 22 14"><path d="M2 2l9 9 9-9" fill="none" stroke="#fff" stroke-width="3"/></svg></span>
  </div>
  <div class="bio-body">
    <h3>TobiV Photography</h3>
    <p><strong>Function : Head promotions, photographer, communication, marketing, and sales.</strong></p>
    <p><strong>Active since : Jan 2006</strong></p>
    <p><strong>Shoots : 500 and counting</strong></p>
    <p><strong>Wil jij fotograferen voor Brindlepost?</strong></p>
    <p>Als je uitgaan leuk vindt, makkelijk bent in de omgang en uitstekend houdt van fotograferen, biedt Brindlepost je de kans een kijkje te nemen in de wereld van de partyfotografie. Door de inzet van de fotografen is Brindlepost uitgegroeid tot een van de meest toonaangevende partysites van Nederland. De betrouwbaarheid, de hoge kwaliteit van de foto's en het covered van de belangrijkste evenementen maakt van Brindlepost een van de best bezochte websites in ons vakgebied.</p>
    <p><strong>Belangrijk informatie</strong></p>
    <p>Fotograferen voor Brindlepost is op vrijwillige basis. Je kan kiezen waar en wanneer je uitgaat en foto's maakt, maar een vaste inbreng word wel van je verwacht. Hoe meer je voor Brindlepost doet, hoe meer ervaring je opdoet met de camera en hoe beter je wordt. Hierdoor kan je weer naar interessantere feesten en festivals. Wat je wel krijgt is gratis entree voor een evenement en soms ook andere voordelen zoals gratis drankjes... Je gaat meestal met ze tweetjes op pad en ontmoet veel nieuwe mensen zoals DJ's en organisatoren. Hoe meer je voor Brindlepost hebt gewerkt hoe meer ervaring je er ook uit zal halen. De beste fotografen doen de leukste en de meest uitdagende evenementen bijvoorbeeld: Hal Negen, Buitenland Outdoor, Zonnegloed weekend, Meerdans etc.</p>
    <p><strong>Voorwaarden</strong></p>
    <p>- Je moet 18 jaar of ouder zijn.<br>- Je moet het aankunnen om hoge kwaliteit foto's te maken en professioneel gedrag vertonen.<br>- Je moet sociaal zijn; een open persoon zijn die ervan houdt om andere mensen te ontmoeten.<br>- Het is een vereiste dat je een digitale spiegelreflex-camera hebt en lichtsterke lens met vast diafragma van F2.8 en natuurlijk een externe flitser (E-TTL).<br>- Je bent verantwoordelijk voor je eigen vervoer om naar de evenementen te gaan waar je foto's maakt.</p>
    <p><strong>Aanmelden</strong><br>Wil jij ook het team van Brindlepost versterken en het nachtleven van een andere kant verkennen? Geef je dan op, stuur een mailtje naar crew@brindlepost.example Vermeld daar goed in je naam, leeftijd, woonplaats en het type camera dat je hebt en je ervaring op het gebied van fotograferen.</p>
    <p>Bekijk ons online foto album voor de door mij geschoten foto's. Bekijk al mijn filmpjes via mijn eigen videokanaal</p>
  </div>
</section>

<section class="section events">
  <div class="section-head">Geplande evenementen (18)
    <span class="toggle"><svg width="22" height="14" viewBox="0 0 22 14"><path d="M2 2l9 9 9-9" fill="none" stroke="#fff" stroke-width="3"/></svg></span>
  </div>
  <div class="event-list">
    <article class="event"><div class="poster p-green" role="img" aria-label="Poster van het Zomerplein festival"><span class="date">20 augustus 2016</span></div>
      <div class="event-text"><div class="event-title">Recreatiegebied Veldmeer</div>
        <div class="event-row"><svg viewBox="0 0 14 14"><path d="M7 1a4.5 4.5 0 0 0-4.5 4.5C2.5 9 7 13 7 13s4.5-4 4.5-7.5A4.5 4.5 0 0 0 7 1z" fill="#222"/><circle cx="7" cy="5.5" r="1.6" fill="#fff"/></svg>Sportpark Lindenhof, Amsterdam</div>
        <div class="event-row"><svg viewBox="0 0 14 14"><path d="M5 2l7-1.5v9" fill="none" stroke="#222" stroke-width="1.6"/><path d="M5 2v9" stroke="#222" stroke-width="1.6"/><circle cx="3.5" cy="11" r="2" fill="#222"/><circle cx="10.5" cy="9.5" r="2" fill="#222"/></svg>Live / Soul / Techno / Uk</div>
        <div class="event-row"><svg viewBox="0 0 14 14"><circle cx="7" cy="7" r="6" fill="#222"/><path d="M7 3.5V7l2.5 1.5" fill="none" stroke="#fff" stroke-width="1.5"/></svg>12.00 – 23.00 uur</div>
        <div class="event-row"><svg viewBox="0 0 14 14"><path d="M1 1h6l6 6-6 6-6-6z" fill="#222"/><circle cx="4" cy="4" r="1.2" fill="#fff"/></svg>Pre-register now for KADEWERK Festival 2016 at: - http://kadewerkfestival.example/</div>
      </div></article>
    <article class="event"><div class="poster p-teal" role="img" aria-label="Poster van Kadewerk Festival"><span class="date">20 augustus 2016</span></div>
      <div class="event-text"><div class="event-title">Kadewerk Festival 2016</div>
        <div class="event-row"><svg viewBox="0 0 14 14"><path d="M7 1a4.5 4.5 0 0 0-4.5 4.5C2.5 9 7 13 7 13s4.5-4 4.5-7.5A4.5 4.5 0 0 0 7 1z" fill="#222"/><circle cx="7" cy="5.5" r="1.6" fill="#fff"/></svg>Sportpark Lindenhof, Amsterdam</div>
        <div class="event-row"><svg viewBox="0 0 14 14"><path d="M5 2l7-1.5v9" fill="none" stroke="#222" stroke-width="1.6"/><path d="M5 2v9" stroke="#222" stroke-width="1.6"/><circle cx="3.5" cy="11" r="2" fill="#222"/><circle cx="10.5" cy="9.5" r="2" fill="#222"/></svg>Live / Soul / Techno / Uk</div>
        <div class="event-row"><svg viewBox="0 0 14 14"><circle cx="7" cy="7" r="6" fill="#222"/><path d="M7 3.5V7l2.5 1.5" fill="none" stroke="#fff" stroke-width="1.5"/></svg>12.00 – 23.00 uur</div>
        <div class="event-row"><svg viewBox="0 0 14 14"><path d="M1 1h6l6 6-6 6-6-6z" fill="#222"/><circle cx="4" cy="4" r="1.2" fill="#fff"/></svg>Pre-register now for KADEWERK Festival 2016 at: - http://kadewerkfestival.example/</div>
      </div></article>
    <article class="event"><div class="poster p-green" role="img" aria-label="Poster van het Zomerplein festival"><span class="date">20 augustus 2016</span></div>
      <div class="event-text"><div class="event-title">Recreatiegebied Veldmeer</div>
        <div class="event-row"><svg viewBox="0 0 14 14"><path d="M7 1a4.5 4.5 0 0 0-4.5 4.5C2.5 9 7 13 7 13s4.5-4 4.5-7.5A4.5 4.5 0 0 0 7 1z" fill="#222"/><circle cx="7" cy="5.5" r="1.6" fill="#fff"/></svg>Sportpark Lindenhof, Amsterdam</div>
        <div class="event-row"><svg viewBox="0 0 14 14"><path d="M5 2l7-1.5v9" fill="none" stroke="#222" stroke-width="1.6"/><path d="M5 2v9" stroke="#222" stroke-width="1.6"/><circle cx="3.5" cy="11" r="2" fill="#222"/><circle cx="10.5" cy="9.5" r="2" fill="#222"/></svg>Live / Soul / Techno / Uk</div>
        <div class="event-row"><svg viewBox="0 0 14 14"><circle cx="7" cy="7" r="6" fill="#222"/><path d="M7 3.5V7l2.5 1.5" fill="none" stroke="#fff" stroke-width="1.5"/></svg>12.00 – 23.00 uur</div>
        <div class="event-row"><svg viewBox="0 0 14 14"><path d="M1 1h6l6 6-6 6-6-6z" fill="#222"/><circle cx="4" cy="4" r="1.2" fill="#fff"/></svg>Pre-register now for KADEWERK Festival 2016 at: - http://kadewerkfestival.example/</div>
      </div></article>
    <article class="event"><div class="poster p-teal" role="img" aria-label="Poster van Kadewerk Festival"><span class="date">20 augustus 2016</span></div>
      <div class="event-text"><div class="event-title">Kadewerk Festival 2016</div>
        <div class="event-row"><svg viewBox="0 0 14 14"><path d="M7 1a4.5 4.5 0 0 0-4.5 4.5C2.5 9 7 13 7 13s4.5-4 4.5-7.5A4.5 4.5 0 0 0 7 1z" fill="#222"/><circle cx="7" cy="5.5" r="1.6" fill="#fff"/></svg>Sportpark Lindenhof, Amsterdam</div>
        <div class="event-row"><svg viewBox="0 0 14 14"><path d="M5 2l7-1.5v9" fill="none" stroke="#222" stroke-width="1.6"/><path d="M5 2v9" stroke="#222" stroke-width="1.6"/><circle cx="3.5" cy="11" r="2" fill="#222"/><circle cx="10.5" cy="9.5" r="2" fill="#222"/></svg>Live / Soul / Techno / Uk</div>
        <div class="event-row"><svg viewBox="0 0 14 14"><circle cx="7" cy="7" r="6" fill="#222"/><path d="M7 3.5V7l2.5 1.5" fill="none" stroke="#fff" stroke-width="1.5"/></svg>12.00 – 23.00 uur</div>
        <div class="event-row"><svg viewBox="0 0 14 14"><path d="M1 1h6l6 6-6 6-6-6z" fill="#222"/><circle cx="4" cy="4" r="1.2" fill="#fff"/></svg>Pre-register now for KADEWERK Festival 2016 at: - http://kadewerkfestival.example/</div>
      </div></article>
    <article class="event"><div class="poster p-green" role="img" aria-label="Poster van het Zomerplein festival"><span class="date">20 augustus 2016</span></div>
      <div class="event-text"><div class="event-title">Recreatiegebied Veldmeer</div>
        <div class="event-row"><svg viewBox="0 0 14 14"><path d="M7 1a4.5 4.5 0 0 0-4.5 4.5C2.5 9 7 13 7 13s4.5-4 4.5-7.5A4.5 4.5 0 0 0 7 1z" fill="#222"/><circle cx="7" cy="5.5" r="1.6" fill="#fff"/></svg>Sportpark Lindenhof, Amsterdam</div>
        <div class="event-row"><svg viewBox="0 0 14 14"><path d="M5 2l7-1.5v9" fill="none" stroke="#222" stroke-width="1.6"/><path d="M5 2v9" stroke="#222" stroke-width="1.6"/><circle cx="3.5" cy="11" r="2" fill="#222"/><circle cx="10.5" cy="9.5" r="2" fill="#222"/></svg>Live / Soul / Techno / Uk</div>
        <div class="event-row"><svg viewBox="0 0 14 14"><circle cx="7" cy="7" r="6" fill="#222"/><path d="M7 3.5V7l2.5 1.5" fill="none" stroke="#fff" stroke-width="1.5"/></svg>12.00 – 23.00 uur</div>
        <div class="event-row"><svg viewBox="0 0 14 14"><path d="M1 1h6l6 6-6 6-6-6z" fill="#222"/><circle cx="4" cy="4" r="1.2" fill="#fff"/></svg>Pre-register now for KADEWERK Festival 2016 at: - http://kadewerkfestival.example/</div>
      </div></article>
    <article class="event"><div class="poster p-green" role="img" aria-label="Poster van het Zomerplein festival"><span class="date">20 augustus 2016</span></div>
      <div class="event-text"><div class="event-title">Recreatiegebied Veldmeer</div>
        <div class="event-row"><svg viewBox="0 0 14 14"><path d="M7 1a4.5 4.5 0 0 0-4.5 4.5C2.5 9 7 13 7 13s4.5-4 4.5-7.5A4.5 4.5 0 0 0 7 1z" fill="#222"/><circle cx="7" cy="5.5" r="1.6" fill="#fff"/></svg>Sportpark Lindenhof, Amsterdam</div>
        <div class="event-row"><svg viewBox="0 0 14 14"><path d="M5 2l7-1.5v9" fill="none" stroke="#222" stroke-width="1.6"/><path d="M5 2v9" stroke="#222" stroke-width="1.6"/><circle cx="3.5" cy="11" r="2" fill="#222"/><circle cx="10.5" cy="9.5" r="2" fill="#222"/></svg>Live / Soul / Techno / Uk</div>
        <div class="event-row"><svg viewBox="0 0 14 14"><circle cx="7" cy="7" r="6" fill="#222"/><path d="M7 3.5V7l2.5 1.5" fill="none" stroke="#fff" stroke-width="1.5"/></svg>12.00 – 23.00 uur</div>
        <div class="event-row"><svg viewBox="0 0 14 14"><path d="M1 1h6l6 6-6 6-6-6z" fill="#222"/><circle cx="4" cy="4" r="1.2" fill="#fff"/></svg>Pre-register now for KADEWERK Festival 2016 at: - http://kadewerkfestival.example/</div>
      </div></article>
    <article class="event"><div class="poster p-teal" role="img" aria-label="Poster van Kadewerk Festival"><span class="date">20 augustus 2016</span></div>
      <div class="event-text"><div class="event-title">Kadewerk Festival 2016</div>
        <div class="event-row"><svg viewBox="0 0 14 14"><path d="M7 1a4.5 4.5 0 0 0-4.5 4.5C2.5 9 7 13 7 13s4.5-4 4.5-7.5A4.5 4.5 0 0 0 7 1z" fill="#222"/><circle cx="7" cy="5.5" r="1.6" fill="#fff"/></svg>Sportpark Lindenhof, Amsterdam</div>
        <div class="event-row"><svg viewBox="0 0 14 14"><path d="M5 2l7-1.5v9" fill="none" stroke="#222" stroke-width="1.6"/><path d="M5 2v9" stroke="#222" stroke-width="1.6"/><circle cx="3.5" cy="11" r="2" fill="#222"/><circle cx="10.5" cy="9.5" r="2" fill="#222"/></svg>Live / Soul / Techno / Uk</div>
        <div class="event-row"><svg viewBox="0 0 14 14"><circle cx="7" cy="7" r="6" fill="#222"/><path d="M7 3.5V7l2.5 1.5" fill="none" stroke="#fff" stroke-width="1.5"/></svg>12.00 – 23.00 uur</div>
        <div class="event-row"><svg viewBox="0 0 14 14"><path d="M1 1h6l6 6-6 6-6-6z" fill="#222"/><circle cx="4" cy="4" r="1.2" fill="#fff"/></svg>Pre-register now for KADEWERK Festival 2016 at: - http://kadewerkfestival.example/</div>
      </div></article>
  </div>
</section>

<section class="section events">
  <div class="section-head">Geplande evenementen (18)
    <span class="toggle"><svg width="22" height="14" viewBox="0 0 22 14"><path d="M2 2l9 9 9-9" fill="none" stroke="#fff" stroke-width="3"/></svg></span>
  </div>
  <div class="event-list">
    <article class="event"><div class="poster p-bright" role="img" aria-label="Poster van Buitenland Outdoor"><span class="date">20 augustus 2016</span></div>
      <div class="event-text"><div class="event-title">Recreatiegebied Veldmeer</div>
        <div class="event-row"><svg viewBox="0 0 14 14"><path d="M7 1a4.5 4.5 0 0 0-4.5 4.5C2.5 9 7 13 7 13s4.5-4 4.5-7.5A4.5 4.5 0 0 0 7 1z" fill="#222"/><circle cx="7" cy="5.5" r="1.6" fill="#fff"/></svg>Sportpark Lindenhof, Amsterdam</div>
        <div class="event-row"><svg viewBox="0 0 14 14"><path d="M5 2l7-1.5v9" fill="none" stroke="#222" stroke-width="1.6"/><path d="M5 2v9" stroke="#222" stroke-width="1.6"/><circle cx="3.5" cy="11" r="2" fill="#222"/><circle cx="10.5" cy="9.5" r="2" fill="#222"/></svg>Live / Soul / Techno / Uk</div>
        <div class="event-row"><svg viewBox="0 0 14 14"><circle cx="7" cy="7" r="6" fill="#222"/><path d="M7 3.5V7l2.5 1.5" fill="none" stroke="#fff" stroke-width="1.5"/></svg>12.00 – 23.00 uur</div>
        <div class="event-row"><svg viewBox="0 0 14 14"><path d="M1 1h6l6 6-6 6-6-6z" fill="#222"/><circle cx="4" cy="4" r="1.2" fill="#fff"/></svg>Pre-register now for KADEWERK Festival 2016 at: - http://kadewerkfestival.example/</div>
      </div></article>
    <article class="event"><div class="poster p-navy" role="img" aria-label="Poster van Zonnegloed"><span class="date">20 augustus 2016</span></div>
      <div class="event-text"><div class="event-title">Kadewerk Festival 2016</div>
        <div class="event-row"><svg viewBox="0 0 14 14"><path d="M7 1a4.5 4.5 0 0 0-4.5 4.5C2.5 9 7 13 7 13s4.5-4 4.5-7.5A4.5 4.5 0 0 0 7 1z" fill="#222"/><circle cx="7" cy="5.5" r="1.6" fill="#fff"/></svg>Sportpark Lindenhof, Amsterdam</div>
        <div class="event-row"><svg viewBox="0 0 14 14"><path d="M5 2l7-1.5v9" fill="none" stroke="#222" stroke-width="1.6"/><path d="M5 2v9" stroke="#222" stroke-width="1.6"/><circle cx="3.5" cy="11" r="2" fill="#222"/><circle cx="10.5" cy="9.5" r="2" fill="#222"/></svg>Live / Soul / Techno / Uk</div>
        <div class="event-row"><svg viewBox="0 0 14 14"><circle cx="7" cy="7" r="6" fill="#222"/><path d="M7 3.5V7l2.5 1.5" fill="none" stroke="#fff" stroke-width="1.5"/></svg>12.00 – 23.00 uur</div>
        <div class="event-row"><svg viewBox="0 0 14 14"><path d="M1 1h6l6 6-6 6-6-6z" fill="#222"/><circle cx="4" cy="4" r="1.2" fill="#fff"/></svg>Pre-register now for KADEWERK Festival 2016 at: - http://kadewerkfestival.example/</div>
      </div></article>
    <article class="event"><div class="poster p-bright" role="img" aria-label="Poster van Buitenland Outdoor"><span class="date">20 augustus 2016</span></div>
      <div class="event-text"><div class="event-title">Recreatiegebied Veldmeer</div>
        <div class="event-row"><svg viewBox="0 0 14 14"><path d="M7 1a4.5 4.5 0 0 0-4.5 4.5C2.5 9 7 13 7 13s4.5-4 4.5-7.5A4.5 4.5 0 0 0 7 1z" fill="#222"/><circle cx="7" cy="5.5" r="1.6" fill="#fff"/></svg>Sportpark Lindenhof, Amsterdam</div>
        <div class="event-row"><svg viewBox="0 0 14 14"><path d="M5 2l7-1.5v9" fill="none" stroke="#222" stroke-width="1.6"/><path d="M5 2v9" stroke="#222" stroke-width="1.6"/><circle cx="3.5" cy="11" r="2" fill="#222"/><circle cx="10.5" cy="9.5" r="2" fill="#222"/></svg>Live / Soul / Techno / Uk</div>
        <div class="event-row"><svg viewBox="0 0 14 14"><circle cx="7" cy="7" r="6" fill="#222"/><path d="M7 3.5V7l2.5 1.5" fill="none" stroke="#fff" stroke-width="1.5"/></svg>12.00 – 23.00 uur</div>
        <div class="event-row"><svg viewBox="0 0 14 14"><path d="M1 1h6l6 6-6 6-6-6z" fill="#222"/><circle cx="4" cy="4" r="1.2" fill="#fff"/></svg>Pre-register now for KADEWERK Festival 2016 at: - http://kadewerkfestival.example/</div>
      </div></article>
    <article class="event"><div class="poster p-navy" role="img" aria-label="Poster van Zonnegloed"><span class="date">20 augustus 2016</span></div>
      <div class="event-text"><div class="event-title">Kadewerk Festival 2016</div>
        <div class="event-row"><svg viewBox="0 0 14 14"><path d="M7 1a4.5 4.5 0 0 0-4.5 4.5C2.5 9 7 13 7 13s4.5-4 4.5-7.5A4.5 4.5 0 0 0 7 1z" fill="#222"/><circle cx="7" cy="5.5" r="1.6" fill="#fff"/></svg>Sportpark Lindenhof, Amsterdam</div>
        <div class="event-row"><svg viewBox="0 0 14 14"><path d="M5 2l7-1.5v9" fill="none" stroke="#222" stroke-width="1.6"/><path d="M5 2v9" stroke="#222" stroke-width="1.6"/><circle cx="3.5" cy="11" r="2" fill="#222"/><circle cx="10.5" cy="9.5" r="2" fill="#222"/></svg>Live / Soul / Techno / Uk</div>
        <div class="event-row"><svg viewBox="0 0 14 14"><circle cx="7" cy="7" r="6" fill="#222"/><path d="M7 3.5V7l2.5 1.5" fill="none" stroke="#fff" stroke-width="1.5"/></svg>12.00 – 23.00 uur</div>
        <div class="event-row"><svg viewBox="0 0 14 14"><path d="M1 1h6l6 6-6 6-6-6z" fill="#222"/><circle cx="4" cy="4" r="1.2" fill="#fff"/></svg>Pre-register now for KADEWERK Festival 2016 at: - http://kadewerkfestival.example/</div>
      </div></article>
    <article class="event"><div class="poster p-bright" role="img" aria-label="Poster van Buitenland Outdoor"><span class="date">20 augustus 2016</span></div>
      <div class="event-text"><div class="event-title">Recreatiegebied Veldmeer</div>
        <div class="event-row"><svg viewBox="0 0 14 14"><path d="M7 1a4.5 4.5 0 0 0-4.5 4.5C2.5 9 7 13 7 13s4.5-4 4.5-7.5A4.5 4.5 0 0 0 7 1z" fill="#222"/><circle cx="7" cy="5.5" r="1.6" fill="#fff"/></svg>Sportpark Lindenhof, Amsterdam</div>
        <div class="event-row"><svg viewBox="0 0 14 14"><path d="M5 2l7-1.5v9" fill="none" stroke="#222" stroke-width="1.6"/><path d="M5 2v9" stroke="#222" stroke-width="1.6"/><circle cx="3.5" cy="11" r="2" fill="#222"/><circle cx="10.5" cy="9.5" r="2" fill="#222"/></svg>Live / Soul / Techno / Uk</div>
        <div class="event-row"><svg viewBox="0 0 14 14"><circle cx="7" cy="7" r="6" fill="#222"/><path d="M7 3.5V7l2.5 1.5" fill="none" stroke="#fff" stroke-width="1.5"/></svg>12.00 – 23.00 uur</div>
        <div class="event-row"><svg viewBox="0 0 14 14"><path d="M1 1h6l6 6-6 6-6-6z" fill="#222"/><circle cx="4" cy="4" r="1.2" fill="#fff"/></svg>Pre-register now for KADEWERK Festival 2016 at: - http://kadewerkfestival.example/</div>
      </div></article>
  </div>
</section>

<section class="section photos">
  <div class="section-head">Foto's (575)
    <span class="toggle"><svg width="22" height="14" viewBox="0 0 22 14"><path d="M2 2l9 9 9-9" fill="none" stroke="#fff" stroke-width="3"/></svg></span>
  </div>
  <div class="photo-grid">
    <div class="tall" role="img" aria-label="Partyfoto van feestgangers in oranje kleding"></div>
    <div class="alt" role="img" aria-label="Partyfoto op straat"></div>
    <div role="img" aria-label="Partyfoto van een groep vrienden"></div>
    <div class="alt" role="img" aria-label="Partyfoto bij een gracht"></div>
    <div role="img" aria-label="Partyfoto van feestgangers"></div>
    <div class="dark" role="img" aria-label="Partyfoto binnen"></div>
    <div class="dark" role="img" aria-label="Partyfoto van twee gasten"></div>
    <div role="img" aria-label="Partyfoto in oranje"></div>
    <div class="alt" role="img" aria-label="Partyfoto op een plein"></div>
    <div class="tall" role="img" aria-label="Partyfoto van feestgangers in oranje kleding"></div>
    <div role="img" aria-label="Partyfoto van een groep"></div>
    <div class="alt" role="img" aria-label="Partyfoto op straat"></div>
    <div role="img" aria-label="Partyfoto van gasten"></div>
    <div class="dark" role="img" aria-label="Partyfoto bij de bar"></div>
    <div role="img" aria-label="Partyfoto van vrienden"></div>
    <div class="alt" role="img" aria-label="Partyfoto buiten"></div>
    <div role="img" aria-label="Partyfoto van feestgangers"></div>
    <div class="dark" role="img" aria-label="Partyfoto op een boot"></div>
  </div>
</section>

<footer class="footer">
  <div class="footer-links">CONTACT &nbsp;|&nbsp; GEBRUIKERSVOORWAARDEN &nbsp;|&nbsp; PRIVACY POLICY</div>
  <div class="footer-copy">© 2006 - 2016 Brindlepost</div>
</footer>

</body>
</html>
```